Brook & Thistle Labels*

Hello :) I am needing labels for my herbal tea/petal product. I am a small producer for the local restaurants (edible flowers/micro herbs & dried product). I am hoping to sell the dried product online. It will be sold in batches as it is ready so quite small/boutique and the label needs to be somewhat generic for the range of produce I make.
Feels: no/minimal plastic, product is in a reusable mason jar, we use organic/regenerative principles from soil health to end product. Treading gently on the land. High quality i.e only fresh hand picked leaf tips for the tea.

```html
<!DOCTYPE html>
<html lang="en">
<head>
<meta charset="utf-8">
<title>Brook &amp; Thistle – Herbal Tea Label</title>
<link rel="stylesheet" href="https://fonts.googleapis.com/css2?family=Montserrat:wght@600&family=Josefin+Sans:wght@300;400&family=Parisienne&display=swap">
<style>
  :root {
    --page: #ffffff;
    --paper: #e9e7dc;
    --green: #5b7150;
    --green-text: #4f6646;
    --sketch: #c9cfbd;
    --tag-text: #e9e7dc;
  }
  html, body {
    margin: 0;
    padding: 0;
    width: 1200px;
    height: 675px;
    overflow: hidden;
    background: var(--page);
  }
  .canvas {
    position: relative;
    width: 1200px;
    height: 675px;
  }
  .label {
    position: absolute;
    left: 378px;
    top: 56px;
    width: 444px;
    height: 562px;
    background: var(--paper);
    box-shadow: 0 1px 4px rgba(0,0,0,0.12);
  }
  .label-frame {
    position: absolute;
    inset: 10px;
    border: 1.5px solid var(--green);
  }
  .brand {
    position: absolute;
    left: 116px;
    top: 35px;
    display: flex;
    align-items: center;
    gap: 14px;
  }
  .brand-dot {
    width: 50px;
    height: 50px;
    border-radius: 50%;
    background: var(--green);
  }
  .brand-name {
    font-family: "Montserrat", sans-serif;
    font-weight: 600;
    font-size: 20px;
    color: var(--green);
    letter-spacing: 0.3px;
  }
  .eyebrow {
    position: absolute;
    left: 0;
    width: 100%;
    top: 116px;
    padding-left: 40px;
    box-sizing: border-box;
    text-align: center;
    font-family: "Josefin Sans", sans-serif;
    font-weight: 400;
    font-size: 15px;
    letter-spacing: 2px;
    color: var(--green-text);
  }
  .title {
    position: absolute;
    left: 0;
    width: 100%;
    top: 128px;
    padding-left: 40px;
    box-sizing: border-box;
    text-align: center;
    font-family: "Parisienne", cursive;
    font-size: 54px;
    color: var(--green);
    line-height: 1.1;
  }
  .field-tag {
    position: absolute;
    left: 27px;
    width: 107px;
    height: 28px;
    background: var(--green);
    color: var(--tag-text);
    font-family: "Josefin Sans", sans-serif;
    font-weight: 300;
    font-size: 13px;
    letter-spacing: 1.5px;
    line-height: 30px;
    padding-left: 9px;
    box-sizing: border-box;
  }
  .field-tag--leaf { top: 213px; }
  .field-tag--petals { top: 318px; }
  .field-tag--batch { top: 390px; }
  .options {
    position: absolute;
    left: 180px;
    top: 220px;
    margin: 0;
    padding: 0;
    list-style: none;
    font-family: "Josefin Sans", sans-serif;
    font-weight: 400;
    font-size: 13px;
    letter-spacing: 1.5px;
    color: var(--green-text);
  }
  .options li {
    display: flex;
    align-items: center;
    gap: 8px;
    height: 29px;
  }
  .option-box {
    width: 9px;
    height: 9px;
    border: 1.5px solid var(--green);
    border-radius: 50%;
    margin-top: -3px;
  }
  .rule {
    position: absolute;
    left: 10px;
    width: 424px;
    height: 0;
    border-top: 1.5px solid var(--green);
  }
  .rule--one { top: 302px; }
  .rule--two { top: 374px; }
  .origin {
    position: absolute;
    left: 27px;
    top: 466px;
    font-family: "Josefin Sans", sans-serif;
    font-weight: 400;
    font-size: 13px;
    letter-spacing: 1.5px;
    line-height: 26px;
    color: var(--green-text);
  }
  .botanical {
    position: absolute;
    left: 272px;
    top: 420px;
    width: 118px;
    height: 112px;
  }
</style>
</head>
<body>
<main class="canvas">
  <section class="label">
    <div class="label-frame"></div>

    <div class="brand">
      <span class="brand-dot"></span>
      <span class="brand-name">Brook &amp; Thistle</span>
    </div>

    <div class="eyebrow">SINGLE ORIGIN</div>
    <h1 class="title" style="margin:0;font-weight:400;">Herbal Tea</h1>

    <div class="field-tag field-tag--leaf">LEAF BASE:</div>
    <ul class="options">
      <li><span class="option-box"></span>LEMON VERBENA</li>
      <li><span class="option-box"></span>MINT</li>
      <li><span class="option-box"></span>AGASTACHE</li>
    </ul>

    <div class="rule rule--one"></div>
    <div class="field-tag field-tag--petals">PETALS:</div>

    <div class="rule rule--two"></div>
    <div class="field-tag field-tag--batch">BATCH:</div>

    <div class="origin">WATTLE HOLLOW<br>VICTORIA AUSTRALIA</div>

    <svg class="botanical" role="img" aria-label="Faint line sketch of calendula flowers with leaves" viewBox="0 0 118 112">
      <defs>
        <radialGradient id="botanicalTone" cx="50%" cy="45%" r="55%">
          <stop offset="0%" stop-color="#c9cfbd" stop-opacity="0.8"/>
          <stop offset="100%" stop-color="#e9e7dc" stop-opacity="0"/>
        </radialGradient>
      </defs>
      <rect width="118" height="112" fill="url(#botanicalTone)"/>
    </svg>
  </section>
</main>
</body>
</html>
```